Need business card design for a confectionery company specializing in chocolates. Would like to see designs that use chocolate brown background and lime green wording and logo. Logo preferably chocolate-related.

Target Market(s)

Corporate, Gifts & Occasions, Hotels, Supermarkets, Parties, Events, Weddings

Industry/Entity Type

Food Production

Contact Information for Business Card

Velbrook Confectionery (company name on front of card in lime green)
with words beneath company name saying "chocolates for every occassion" (in lime green in lower case)

Font styles to use
Script

Colors
acd037

Requirements
Must have
• Front of card: Brown background
• Back of card: White background
• Email address on back of card: Info@velbrook.example.zw
• Cellphone number on back of card: 0771 392 615, 0773 581 246
• Address on back of card: 8 Tarnby Close, Marlow Rise, Harare
• ALL WRITING ON BACK OF CARD IN BLACK

```html
<!DOCTYPE html>
<html lang="en">
<head>
<meta charset="utf-8">
<title>Velbrook Confectionery – Business Card</title>
<link href="https://fonts.googleapis.com/css2?family=Grand+Hotel&family=Montserrat:wght@400;600;700&display=swap" rel="stylesheet">
<style>
  :root {
    --chocolate: #4a1a1c;
    --lime: #acd037;
    --paper: #ffffff;
    --ink: #1a1a1a;
    --trim: #9a9a9a;
    --script: "Grand Hotel", cursive;
    --sans: "Montserrat", sans-serif;
  }
  * { margin: 0; padding: 0; box-sizing: border-box; }
  html, body { width: 849px; height: 1200px; overflow: hidden; background: var(--paper); }
  .board { position: relative; width: 849px; height: 1200px; font-family: var(--sans); }

  .top-rule-lime { position: absolute; left: 0; top: 58px; width: 849px; height: 10px; background: var(--lime); }
  .top-rule-brown { position: absolute; left: 0; top: 72px; width: 849px; height: 2px; background: var(--chocolate); }

  .brand { position: absolute; left: 0; top: 170px; width: 849px; text-align: center; }
  .brand-name { font-family: var(--script); color: var(--chocolate); font-size: 78px; line-height: 1; }
  .brand-tagline { margin-top: 14px; font-size: 11px; font-weight: 600; letter-spacing: 0.5px; color: var(--chocolate); }

  .swatch-rule { position: absolute; top: 376px; height: 1px; background: var(--trim); }
  .swatch { position: absolute; top: 370px; width: 34px; height: 34px; }
  .swatch-brown { left: 382px; background: var(--chocolate); }
  .swatch-lime { left: 434px; background: var(--lime); }
  .swatch-label { position: absolute; top: 408px; font-size: 5px; color: var(--trim); }

  .trim-line { position: absolute; height: 1px; background: var(--trim); left: 0; width: 849px; }

  .card { position: absolute; top: 461px; width: 382px; height: 210px; }
  .card-front { left: 37px; background: var(--chocolate); display: flex; flex-direction: column; align-items: center; justify-content: center; }
  .card-front .name { font-family: var(--script); color: var(--lime); font-size: 44px; line-height: 1; }
  .card-front .tagline { margin-top: 8px; font-size: 7px; font-weight: 600; color: var(--lime); }

  .card-back { left: 439px; background: var(--paper); border: 1px solid #d8d8d8; }
  .card-back .mini-brand { position: absolute; left: 26px; top: 86px; font-family: var(--script); color: var(--ink); font-size: 24px; line-height: 1; }
  .card-back .divider { position: absolute; left: 156px; top: 62px; width: 1px; height: 84px; background: var(--ink); }
  .card-back .person { position: absolute; left: 170px; top: 74px; font-size: 15px; font-weight: 700; color: var(--ink); }
  .card-back .details { position: absolute; left: 170px; top: 98px; font-size: 6.4px; line-height: 1.6; color: var(--ink); }

  .scene-fill { position: absolute; left: 0; top: 792px; width: 849px; height: 408px;
    background: linear-gradient(135deg, #3e1517 0%, #5a2326 45%, #e9e4e1 46%, #4a1a1c 60%, #3a1416 100%); }
</style>
</head>
<body>
<div class="board">
  <div class="top-rule-lime"></div>
  <div class="top-rule-brown"></div>

  <div class="brand">
    <div class="brand-name">Velbrook Confectionery</div>
    <div class="brand-tagline">chocolates for every occasion</div>
  </div>

  <div class="swatch-rule" style="left:0;width:370px"></div>
  <div class="swatch-rule" style="left:480px;width:369px"></div>
  <div class="swatch swatch-brown"></div>
  <div class="swatch swatch-lime"></div>
  <div class="swatch-label" style="left:390px">BROWN</div>
  <div class="swatch-label" style="left:444px">LIME</div>

  <div class="trim-line" style="top:439px"></div>
  <div class="trim-line" style="top:694px"></div>

  <div class="card card-front">
    <div class="name">Velbrook Confectionery</div>
    <div class="tagline">chocolates for every occasion</div>
  </div>

  <div class="card card-back">
    <div class="mini-brand">Velbrook<br>Confectionery</div>
    <div class="divider"></div>
    <div class="person">Rudo Chikanda</div>
    <div class="details">
      Address: 8 Tarnby Close, Marlow Rise, Harare<br>
      Contact: 0771 392 615 / 0773 581 246<br>
      Email: Info@velbrook.example.zw
    </div>
  </div>

  <div class="scene-fill" role="img" aria-label="Photograph of many printed brown and white business cards scattered in a pile"></div>
</div>
</body>
</html>
```